New Packaging Design Project

Wine packaging redesign. Retail partner requested a redesign of a private label wine. The old label is attached. Our partner liked the Lantern and Briar label and wanted something similar. There will be a logo added to the top of the label

Went on vacation/holiday

```html
<!DOCTYPE html>
<html lang="en">
<head>
<meta charset="utf-8">
<title>Napa Valley Red Blend – Label Concepts</title>
<link rel="stylesheet" href="https://fonts.googleapis.com/css2?family=Encode+Sans+Condensed:wght@300;400;500&display=swap">
<style>
  :root {
    --backdrop: #a9a3a0;
    --backdrop-light: #c6c1be;
    --divider: #ffffff;
    --label: #3a3a3b;
    --label-edge: #2f2f30;
    --gold: #cfb06a;
    --gold-deep: #8a7444;
    --ink-light: #e4e2de;
    --rule: #f2f0ec;
    --hill-far: #2c2c2d;
    --hill-mid: #474748;
    --hill-near: #5a5a5b;
    --field: #3f3f40;
  }

  * { box-sizing: border-box; margin: 0; padding: 0; }

  html, body {
    width: 799px;
    height: 1200px;
    overflow: hidden;
  }

  body {
    background: var(--backdrop);
    font-family: "Encode Sans Condensed", "Arial Narrow", sans-serif;
  }

  .concept-sheet {
    width: 799px;
    height: 1200px;
    display: flex;
    flex-direction: column;
  }

  .concept {
    position: relative;
    height: 600px;
    display: flex;
    align-items: center;
    justify-content: center;
    background: radial-gradient(ellipse at 30% 45%, var(--backdrop-light) 0%, var(--backdrop) 70%);
  }

  .concept + .concept {
    border-top: 2px solid var(--divider);
  }

  .wine-label {
    width: 420px;
    height: 500px;
    background: var(--label);
    border: 1px solid var(--label-edge);
    display: flex;
    flex-direction: column;
    align-items: center;
    padding-top: 44px;
    overflow: hidden;
    box-shadow: 0 10px 30px rgba(0, 0, 0, 0.25);
  }

  .wine-label__region {
    color: var(--gold);
    font-weight: 300;
    font-size: 40px;
    letter-spacing: 7px;
    line-height: 1;
    text-transform: uppercase;
  }

  .wine-label__style {
    margin-top: 8px;
    color: var(--gold);
    font-weight: 400;
    font-size: 22px;
    letter-spacing: 0.5px;
    text-transform: uppercase;
  }

  .wine-label__rule {
    width: 44px;
    height: 2px;
    margin: 14px 0 16px;
    background: var(--rule);
    border: none;
  }

  .wine-label__varietals {
    color: var(--ink-light);
    font-size: 13px;
    letter-spacing: 0.4px;
    line-height: 1.75;
    text-align: center;
    text-transform: uppercase;
  }

  .wine-label__vintage {
    margin-top: 8px;
    color: var(--gold);
    font-size: 12px;
    letter-spacing: 0.5px;
  }

  .wine-label__scene {
    margin-top: 22px;
    width: 100%;
    flex: 1;
  }

  .wine-label__scene--line {
    background:
      linear-gradient(180deg,
        var(--label) 0%,
        #3e3c38 18%,
        #4a4436 45%,
        #5a4e34 70%,
        var(--gold-deep) 100%);
  }

  .wine-label__scene--silhouette {
    background:
      linear-gradient(180deg,
        var(--label) 0%,
        var(--hill-far) 14%,
        var(--hill-far) 30%,
        var(--hill-mid) 44%,
        var(--hill-near) 58%,
        var(--field) 72%,
        #4a4538 88%,
        var(--gold-deep) 100%);
  }
</style>
</head>
<body>
  <main class="concept-sheet">
    <section class="concept concept--line-art">
      <article class="wine-label">
        <h1 class="wine-label__region">Napa Valley</h1>
        <p class="wine-label__style">Red Blend</p>
        <hr class="wine-label__rule">
        <p class="wine-label__varietals">Merlot | Cabernet Sauvignon<br>Cabernet Franc | Petit Verdot | Malbec</p>
        <p class="wine-label__vintage">2018</p>
        <div class="wine-label__scene wine-label__scene--line" role="img" aria-label="Gold line-art landscape of a mountain ridge, rolling hills, rounded trees and curving vineyard rows"></div>
      </article>
    </section>

    <section class="concept concept--silhouette">
      <article class="wine-label">
        <h1 class="wine-label__region">Napa Valley</h1>
        <p class="wine-label__style">Red Blend</p>
        <hr class="wine-label__rule">
        <p class="wine-label__varietals">Merlot | Cabernet Sauvignon<br>Cabernet Franc | Petit Verdot | Malbec</p>
        <p class="wine-label__vintage">2018</p>
        <div class="wine-label__scene wine-label__scene--silhouette" role="img" aria-label="Layered grey mountain and hill silhouettes above gold curving vineyard row lines"></div>
      </article>
    </section>
  </main>
</body>
</html>
```